#LUMA

#Luma is the business name. I need a marketing brochure to show potential clients. The concept is providing the restaurant trade and function centres with volume wine in large wine casks and then on-sell by the glass or in varying carafe sizes. The advantages will be outlined in the file provided I want to introduce the concept and demonstrate the advantages visusally

Restaurant

```html
<!DOCTYPE html>
<html lang="en">
<head>
<meta charset="utf-8">
<title>#LUMA – Volume Wine for the Restaurant Trade</title>
<link rel="stylesheet" href="https://fonts.googleapis.com/css2?family=Libre+Franklin:wght@400;500;600&display=swap">
<style>
  :root {
    --wine-red: #83242a;
    --ivory: #ffffff;
  }
  html, body {
    margin: 0;
    padding: 0;
    overflow: hidden;
    background: var(--wine-red);
  }
  .brochure {
    position: relative;
    width: 998px;
    height: 1200px;
    background: var(--wine-red);
    color: var(--ivory);
    font-family: "Libre Franklin", Arial, sans-serif;
    overflow: hidden;
  }
  .brand-title {
    position: absolute;
    left: 46px;
    top: 30px;
    margin: 0;
    font-size: 168px;
    font-weight: 500;
    line-height: 1;
    letter-spacing: -4px;
  }
  .intro {
    position: absolute;
    left: 52px;
    top: 205px;
    width: 640px;
    margin: 0;
    font-size: 38px;
    font-weight: 500;
    line-height: 58px;
  }
  .advantages-heading {
    position: absolute;
    left: 52px;
    top: 487px;
    margin: 0;
    font-size: 42px;
    font-weight: 500;
    line-height: 58px;
  }
  .advantages-list {
    position: absolute;
    left: 52px;
    top: 620px;
    width: 650px;
    margin: 0;
    padding: 0;
    list-style: none;
    font-size: 29px;
    font-weight: 500;
    line-height: 35.5px;
  }
  .advantages-list li::before {
    content: "*";
  }
  .bottle-visual {
    position: absolute;
    left: 708px;
    top: 38px;
    width: 270px;
    height: 996px;
    border-radius: 70px 70px 14px 14px;
    background: var(--ivory);
  }
  .product-details {
    position: absolute;
    left: 0;
    top: 1040px;
    width: 998px;
    margin: 0;
    text-align: center;
    font-size: 22px;
    font-weight: 500;
    line-height: 30px;
  }
</style>
</head>
<body>
  <main class="brochure">
    <h1 class="brand-title">#LUMA</h1>
    <p class="intro">Providing the restaurant trade with a more effective, economical and sustainable alternative to wine retail.</p>
    <h2 class="advantages-heading">The advantages of using<br>#LUMA concept:</h2>
    <ul class="advantages-list">
      <li>The cask wine uses less storage space</li>
      <li>Eco friendly, no glass.</li>
      <li>Larger quantity better margins</li>
      <li>Longer shelf life</li>
      <li>No wastage</li>
      <li>More Hygienic</li>
      <li>Wine sourced from reputable growers in well known regions of New Zealand, Barossa Valley and Tasmania.</li>
    </ul>
    <div class="bottle-visual" role="img" aria-label="White wine bottle silhouette with decorative scroll label"></div>
    <p class="product-details">
      Cask sizes will start from 10ltrs and up to 22ltrs<br>
      Aesthetic Urns or Wine barrels to hide cask that will<br>
      come in either 15ltr, 25ltr and will fit all cask sizes.<br>
      Carafe glassware available too: in 250ml, 500ml and 1000ml sizes.
    </p>
  </main>
</body>
</html>
```